UI/UX Re-Do for TallyNest - a free to use project management platform for desktop and mobile.

UI/UX Re-Do for TallyNest
TallyNest is a free to use project management platform for desktop and mobile.
We are looking for help with our UI/UX re-design.
As of now the platform is totally functional.
The problem is around flow and look. We want TN to become something that any one can use to manage and even socialize any project. A project can be something work related like organizing a team around a software build, marketing campaign, shared client file space, etc... In fact, most of our current members are using TN for just such work projects.
We also see a project as planning a wedding, organizing a group trip, a simple to-do list, organizing a kids sports team, and so on...
To become a platform that people will use in their work and personal life we first need to become more intuitive and friendly - while maintaining advanced functionality for more advanced needs.
We need help to beautify, streamline, and simplify - while keeping all the functions.
The quickest way to understand TN, and our current issues is this short video:
https://vidhost.example/Qw8ZmT3pLsK
For sure see this link for the entire most recent description AND images:
https://tallynestapp.example/?p=KumrT4WdZeL
The best way to understand TN is to actually use it:
https://tallynestapp.example
Should you choose to take a run at improving TN here are the details:
Please focus your ideas for mobile, it's where we have the biggest issues.
Feel free to get outside the box.
Avoid swipe oriented designs.
Feel free to focus on ideas over polished outputs.
Use any tool you like, PS, hand drawing, written description if you think that works best.
(FYI - we use mostly use Vellum Slides docs internally)
Point is illustration of ideas over tool choice.
Feel free to:
Create something totally new
And/or riff on what we have now
And/or riff on the new design we are considering (see images below)
|||
If we go the direction of the images/designs below the idea is to give people options on how they see/experience TN.
Just below is what we are calling Base Mode. This is a more basic and simple flow. Probably a default to keep new users feeling comfortable at the start.
<img src="https://picbin.example/8hTzqWL.jpg" style="width: 100%;">
https://picbin.example/8hTzqWL.jpg
|||
We are calling this optional view Peak Mode. It is more advanced and can show all project, goal(renamed 'milestones') at the same time. This is more of a paint job on the current design.
<img src="https://picbin.example/vNmd2Rs.jpg" style="width: 100%;">
https://picbin.example/vNmd2Rs.jpg
|||
If you're submitting please let us know if you can also do the PS files for dev.
Not required, but once we nail down the concepts we want someone to hone in the PS files.
As an optional bonus we will also be giving credit to you/your company in TN.
Let us know if you do or don't want that.
We are excited to see your work!!
Target Market(s)
Anyone who needs to organize any project, big or small. The key is to make a super friendly user experience for new users while retaining advanced functions.
Industry/Entity Type
Management
Number of Pages Required
2 page
Look and feel

```html
<!DOCTYPE html>
<html lang="en">
<head>
<meta charset="utf-8">
<title>TallyNest — Project Tasks</title>
<link rel="stylesheet" href="https://fonts.googleapis.com/css2?family=Montserrat:wght@300;400;500;700&display=swap">
<style>
  :root {
    --bg: #ffffff;
    --floor: #f5f5f5;
    --ink: #1a1a1a;
    --ink-soft: #333333;
    --muted: #8a8a8a;
    --muted-light: #a6a6a6;
    --line: #d6d6d6;
    --accent: #8957b0;
    --badge: #2a86de;
    --danger-icon: #2a86de;
    --fab-red: #ee1c25;
    --pencil: #f2a20f;
    --avatar-1: #8d8d8d;
    --avatar-2: #3a3a3a;
    --avatar-3: #c9a38c;
    --avatar-4: #6f8e86;
    --avatar-5: #b9b3ad;
    --avatar-6: #b8876a;
  }
  * { box-sizing: border-box; margin: 0; padding: 0; }
  html, body { width: 675px; height: 1200px; overflow: hidden; }
  body {
    position: relative;
    background: var(--floor);
    font-family: "Montserrat", Arial, sans-serif;
    color: var(--ink);
  }
  .screen { position: absolute; inset: 0; }

  .app-header {
    position: absolute; left: 0; top: 0; width: 675px; height: 219px;
    background: var(--bg);
    box-shadow: 0 3px 6px rgba(0,0,0,0.12);
    z-index: 2;
  }
  .back-button { position: absolute; left: 33px; top: 55px; }
  .project-title {
    position: absolute; left: 148px; top: 57px;
    font-size: 27px; font-weight: 500; letter-spacing: 0.3px;
  }
  .user-avatar {
    position: absolute; left: 536px; top: 20px; width: 110px; height: 110px;
    border-radius: 50%;
    background: radial-gradient(circle at 50% 40%, #e4c2ab 0 30%, #d9d9d9 31%, #cfcfcf 70%, #34404a 71%);
  }
  .notice-badge {
    position: absolute; left: 618px; top: 25px; width: 30px; height: 30px;
    border-radius: 50%; background: var(--badge); color: #fff;
    font-size: 14px; font-weight: 500; display: flex; align-items: center; justify-content: center;
  }
  .tab-bar { position: absolute; left: 0; top: 166px; width: 675px; height: 53px; }
  .tab {
    position: absolute; top: 0; width: 225px; text-align: center;
    font-size: 27px; font-weight: 500; color: var(--muted-light);
  }
  .tab--overview { left: 0; width: 225px; }
  .tab--tasks { left: 225px; color: var(--accent); }
  .tab--files { left: 468px; width: 225px; }
  .tab-indicator {
    position: absolute; left: 225px; top: 48px; width: 225px; height: 4px; background: var(--accent);
  }

  .task-card { position: absolute; left: 0; top: 219px; width: 675px; height: 274px; background: var(--bg); }
  .task-name { position: absolute; left: 72px; top: 64px; font-size: 17px; font-weight: 500; color: var(--ink-soft); }
  .task-actions { position: absolute; left: 498px; top: 56px; display: flex; gap: 20px; align-items: center; }
  .task-body {
    position: absolute; left: 72px; top: 102px; width: 540px;
    font-size: 17.6px; line-height: 22px; font-weight: 400; color: var(--ink-soft);
  }
  .task-meta {
    position: absolute; left: 72px; top: 200px; display: flex; align-items: center;
    font-size: 18px; color: var(--ink-soft);
  }
  .task-meta span { margin: 0 20px 0 8px; }
  .member-stack { position: absolute; left: 359px; top: 190px; display: flex; gap: 5px; }
  .member { width: 38px; height: 38px; border-radius: 50%; }

  .comments-panel {
    position: absolute; left: 0; top: 493px; width: 675px; height: 647px;
    background: var(--bg); border-top: 1px solid var(--line); border-bottom: 1px solid var(--line);
    border-right: 1px solid var(--line);
  }
  .comments-label {
    position: absolute; left: 90px; top: 16px; font-size: 12px; font-weight: 700;
    letter-spacing: 0.6px; color: var(--muted-light);
  }
  .timeline-rail { position: absolute; left: 89px; top: 78px; width: 1px; bottom: 0; background: var(--line); }
  .comment { position: absolute; left: 0; width: 675px; }
  .comment-dot {
    position: absolute; left: 80px; top: 3px; width: 19px; height: 19px;
    border-radius: 50%; border: 1.5px solid var(--line); background: var(--bg);
  }
  .comment-author { position: absolute; left: 131px; top: 0; font-size: 18px; font-weight: 400; color: var(--ink); white-space: nowrap; }
  .comment-text { position: absolute; left: 131px; top: 22px; font-size: 18px; font-weight: 400; color: var(--muted); white-space: nowrap; }
  .comment-time { position: absolute; left: 533px; font-size: 18px; color: var(--muted-light); }

  .fab { position: absolute; border-radius: 50%; display: flex; align-items: center; justify-content: center; }
  .fab--edit {
    left: 551px; top: 957px; width: 86px; height: 86px; background: var(--bg);
    box-shadow: 0 3px 14px rgba(238,28,37,0.25);
  }
  .fab--add {
    left: 540px; top: 1058px; width: 108px; height: 108px; background: var(--fab-red);
    box-shadow: 0 3px 10px rgba(0,0,0,0.15);
  }
</style>
</head>
<body>
<main class="screen">
  <header class="app-header">
    <svg class="back-button" width="40" height="36" viewBox="0 0 40 36" aria-label="Back">
      <path d="M38 18H4M18 3L3 18l15 15" fill="none" stroke="#777" stroke-width="3"/>
    </svg>
    <h1 class="project-title">Project Title</h1>
    <div class="user-avatar" role="img" aria-label="Profile photo of the signed-in user"></div>
    <div class="notice-badge">5</div>
    <nav class="tab-bar">
      <div class="tab tab--overview">Overview</div>
      <div class="tab tab--tasks">Tasks</div>
      <div class="tab tab--files">Files</div>
      <div class="tab-indicator"></div>
    </nav>
  </header>

  <section class="task-card">
    <h2 class="task-name">Task 1</h2>
    <div class="task-actions">
      <svg width="22" height="22" viewBox="0 0 22 22" aria-label="Edit task"><path d="M3 19l1-5L15 3l4 4L8 18z" fill="#7a7a7a"/></svg>
      <svg width="26" height="24" viewBox="0 0 26 24" aria-label="Share task"><path d="M2 11L24 2 18 22 12 14zM12 14L24 2" fill="none" stroke="#7a7a7a" stroke-width="1.8" stroke-linejoin="round"/></svg>
      <svg width="22" height="26" viewBox="0 0 22 26" aria-label="Delete task"><path d="M2 5h18M8 5V2h6v3M4 5l1 19h12l1-19M9 9v11M13 9v11" fill="none" stroke="var(--danger-icon)" stroke-width="1.8"/></svg>
    </div>
    <p class="task-body">Lorem ipsum dolor sit amet, consectetur adipisicing elit, sed do eiusmod tempor incididunt ut labore et dolore magna aliqua. Ut enim ad minim veniam, quis nostrud exercitation</p>
    <div class="task-meta">
      <svg width="26" height="24" viewBox="0 0 26 24" aria-label="Comments"><path d="M13 2C6.5 2 2 6 2 10.5c0 2.5 1.3 4.6 3.4 6L4 21l5-2.6c1.2.3 2.5.5 4 .5 6.5 0 11-4 11-8.4S19.5 2 13 2z" fill="none" stroke="#555" stroke-width="1.6"/></svg>
      <span>12</span>
      <svg width="22" height="22" viewBox="0 0 22 22" aria-label="Attachments"><path d="M17 9l-7.5 7.5a3 3 0 01-4.2-4.2L13 4.6a2 2 0 012.8 2.8L8.5 14.7" fill="none" stroke="#666" stroke-width="1.6"/></svg>
      <span>5</span>
    </div>
    <div class="member-stack">
      <div class="member" style="background:var(--avatar-1)" role="img" aria-label="Team member photo"></div>
      <div class="member" style="background:var(--avatar-2)" role="img" aria-label="Team member photo"></div>
      <div class="member" style="background:var(--avatar-3)" role="img" aria-label="Team member photo"></div>
      <div class="member" style="background:var(--avatar-4)" role="img" aria-label="Team member photo"></div>
      <div class="member" style="background:var(--avatar-5)" role="img" aria-label="Team member photo"></div>
      <div class="member" style="background:var(--avatar-6)" role="img" aria-label="Team member photo"></div>
    </div>
  </section>

  <section class="comments-panel">
    <h3 class="comments-label">COMMENTS</h3>
    <div class="timeline-rail"></div>
    <article class="comment" style="top:69px">
      <div class="comment-dot"></div>
      <div class="comment-author">Mary Blackwood</div>
      <div class="comment-text">Lorem ipsum dolor sit amet, consectetur</div>
      <div class="comment-time" style="top:-4px">10s</div>
    </article>
    <article class="comment" style="top:141px">
      <div class="comment-dot"></div>
      <div class="comment-author">Tom Burn</div>
      <div class="comment-text">Lorem ipsum dolor sit amet, consectetur</div>
      <div class="comment-time" style="top:3px">3m</div>
    </article>
    <article class="comment" style="top:207px">
      <div class="comment-dot" style="top:7px"></div>
      <div class="comment-author">Mary Blackwood</div>
      <div class="comment-text">Lorem ipsum dolor sit amet,</div>
      <div class="comment-time" style="top:3px">5m</div>
    </article>
    <article class="comment" style="top:279px">
      <div class="comment-dot" style="top:10px"></div>
      <div class="comment-author">John Smith</div>
      <div class="comment-text">Lorem ipsum dolor sit amet,</div>
      <div class="comment-time" style="top:10px">10m</div>
    </article>
    <article class="comment" style="top:363px">
      <div class="comment-dot" style="top:2px"></div>
      <div class="comment-author">John Smith</div>
      <div class="comment-text">Lorem ipsum dolor sit amet, consectetur</div>
      <div class="comment-time" style="top:0">2h</div>
    </article>
  </section>

  <div class="fab fab--edit" aria-label="Write comment">
    <svg width="40" height="40" viewBox="0 0 40 40"><path d="M6 34l2-9L28 5l7 7-20 20z" fill="var(--pencil)"/><path d="M28 5l7 7 2-2a2 2 0 000-3l-4-4a2 2 0 00-3 0z" fill="#e8747a"/><path d="M6 34l2-9 7 7z" fill="#f4d7a8"/></svg>
  </div>
  <div class="fab fab--add" aria-label="Add">
    <svg width="30" height="30" viewBox="0 0 30 30"><path d="M15 2v26M2 15h26" stroke="#fff" stroke-width="3.4"/></svg>
  </div>
</main>
</body>
</html>
```